Adventure Business Cards

Please check out our website for style
Vertical card
Details:
Side 1
Logo
Business name: Kestrel Point Wildland Tours
Name: Colin Warbeck
Role: Director
Email: info@kestrelpointtours.com
Address: PO Box 71, Marlin Cove NSW 2471
Phone: +61 2 5550 1847
Web address: www.kestrelpointtours.com
Side 2
Taking pictures?
A Friendwall and Pixlane logo
Tag us in your pictures with
#kpwildtours
@kpwildtours
www.kestrelpointtours.com
Details:
Side 1
Logo
Name: Colin Warbeck
Role: Director
Phone: +61 2 5550 1847
Side 2
Taking pictures?
#kpwildtours
@kpwildtours

```html
<!DOCTYPE html>
<html lang="en">
<head>
<meta charset="utf-8">
<title>Kestrel Point Wildland Tours – Business Card</title>
<link href="https://fonts.googleapis.com/css2?family=Questrial&family=Fredoka:wght@600&display=swap" rel="stylesheet">
<style>
  :root {
    --page-bg: #e9e6e1;
    --card-top: #ffffff;
    --card-bottom: #ececec;
    --accent: #f0a93a;
    --ink: #2a2a2a;
    --muted: #555555;
    --row: rgba(0,0,0,0.035);
    --badge: #1f2a33;
  }
  * { box-sizing: border-box; margin: 0; padding: 0; }
  html, body { width: 1200px; height: 1023px; overflow: hidden; }
  body {
    background: var(--page-bg);
    font-family: "Questrial", "Century Gothic", sans-serif;
    color: var(--ink);
    position: relative;
  }
  .card {
    position: absolute;
    top: 212px;
    width: 360px;
    height: 600px;
    border-radius: 20px;
    background: linear-gradient(180deg, var(--card-top) 0%, var(--card-bottom) 100%);
    box-shadow: 0 10px 28px rgba(0,0,0,0.18);
    overflow: hidden;
  }
  .card--front { left: 180px; }
  .card--back { left: 660px; }

  /* Front */
  .holder { position: absolute; top: 52px; right: 36px; text-align: right; }
  .holder__name { color: var(--accent); font-size: 26px; font-weight: 700; letter-spacing: 0.5px; }
  .holder__role { color: var(--muted); font-size: 17px; margin-top: 2px; }

  .brand {
    position: absolute; top: 150px; left: 0; right: 0;
    display: flex; flex-direction: column; align-items: center; gap: 14px;
  }
  .brand__dot { width: 70px; height: 70px; border-radius: 50%; background: var(--badge); }
  .brand__name {
    color: var(--ink); font-size: 20px; text-align: center; line-height: 1.3;
    width: 240px;
  }

  .contacts { position: absolute; left: 0; right: 0; top: 340px; list-style: none; }
  .contacts__row {
    display: flex; align-items: center; gap: 14px;
    padding: 0 24px; height: 46px;
    font-size: 16px; color: var(--ink);
  }
  .contacts__row:nth-child(odd) { background: var(--row); }
  .contacts__row--address { height: auto; align-items: flex-start; padding-top: 12px; padding-bottom: 12px; line-height: 1.55; }
  .icon { width: 24px; height: 24px; flex: none; }

  /* Back */
  .back__heading {
    position: absolute; top: 58px; left: 36px;
    font-family: "Fredoka", "Questrial", sans-serif; font-weight: 600;
    font-size: 34px; color: var(--ink);
  }
  .back__lead { position: absolute; top: 128px; left: 36px; right: 30px; font-size: 20px; font-weight: 700; line-height: 1.35; }
  .socials { position: absolute; top: 230px; left: 36px; right: 30px; list-style: none; }
  .socials__row { display: flex; align-items: center; gap: 16px; margin-bottom: 34px; }
  .socials__mark {
    width: 54px; height: 54px; border-radius: 10px; background: var(--badge); flex: none;
  }
  .socials__text { display: flex; flex-direction: column; gap: 4px; }
  .socials__network { font-size: 14px; color: var(--muted); }
  .socials__handle { font-size: 22px; color: var(--ink); }
  .back__web { position: absolute; bottom: 56px; left: 36px; font-size: 18px; color: var(--accent); }
</style>
</head>
<body>

<section class="card card--front" aria-label="Card front">
  <div class="holder">
    <p class="holder__name">Colin Warbeck</p>
    <p class="holder__role">Director</p>
  </div>

  <div class="brand">
    <span class="brand__dot"></span>
    <p class="brand__name">Kestrel Point Wildland Tours</p>
  </div>

  <ul class="contacts">
    <li class="contacts__row">
      <svg class="icon" viewBox="0 0 24 24"><rect x="6" y="2" width="12" height="20" rx="2.5" fill="none" stroke="var(--accent)" stroke-width="1.8"/><circle cx="12" cy="18.5" r="1" fill="var(--accent)"/></svg>
      <span>+61 2 5550 1847</span>
    </li>
    <li class="contacts__row">
      <svg class="icon" viewBox="0 0 24 24"><rect x="2" y="5" width="20" height="14" rx="1.5" fill="var(--accent)"/><path d="M2.5 6 L12 13 L21.5 6" fill="none" stroke="#fff" stroke-width="1.6"/></svg>
      <span>info@kestrelpointtours.com</span>
    </li>
    <li class="contacts__row">
      <svg class="icon" viewBox="0 0 24 24"><circle cx="12" cy="12" r="10" fill="none" stroke="var(--accent)" stroke-width="2.2"/><path d="M2 12 H22 M12 2 C7 7 7 17 12 22 M12 2 C17 7 17 17 12 22" fill="none" stroke="var(--accent)" stroke-width="1.4"/></svg>
      <span>www.kestrelpointtours.com</span>
    </li>
    <li class="contacts__row contacts__row--address">
      <svg class="icon" viewBox="0 0 24 24"><path d="M12 2 C7.5 2 5 5.3 5 9 C5 14 12 22 12 22 C12 22 19 14 19 9 C19 5.3 16.5 2 12 2 Z" fill="var(--accent)"/><circle cx="12" cy="9" r="2.6" fill="#fff"/></svg>
      <span>PO Box 71, Marlin Cove<br>NSW 2471</span>
    </li>
  </ul>
</section>

<section class="card card--back" aria-label="Card back">
  <h2 class="back__heading">Taking pictures?</h2>
  <p class="back__lead">Tag us in your pictures with</p>
  <ul class="socials">
    <li class="socials__row">
      <span class="socials__mark"></span>
      <span class="socials__text"><span class="socials__network">Friendwall</span><span class="socials__handle">#kpwildtours</span></span>
    </li>
    <li class="socials__row">
      <span class="socials__mark"></span>
      <span class="socials__text"><span class="socials__network">Pixlane</span><span class="socials__handle">@kpwildtours</span></span>
    </li>
  </ul>
  <p class="back__web">www.kestrelpointtours.com</p>
</section>

</body>
</html>
```